Icon-Design für App
Zielgruppe
quobarin.com is an app for more social closeness: You can scan people around you (50m) and give quobarins (nobody can see your likes unless you like each other). It's a kind of the opposite of Flurma: Meet first live in a bar, during shopping at the bus-station.... and use the app just as an 'ice-breaker'. Therefore the scanner of quobarin.com is very accurate (50m) and realtime....which is so far unique. We got more than 1000 Users within the first weeks after launch...and it's time to style the app as many people said it looks terrible.... Quobarin is available on appvelo depot or just as a web app in every browser over www.quobarin.com.
Aufgabenstellung
we got many feedbacks that the app-function is great but the design looks terrible. Can you change this? If you tested the app (www.quobarin.com) and once you understood the idea: feel free to follow your feelings when re-designing! We are open to all changes. I actually would like to keep the main logo, the 'shy smiling heart with the hand in front of mouth'...but if you have a better Idea...just do it!

```html
<!DOCTYPE html>
<html lang="en">
<head>
<meta charset="utf-8">
<title>Quobarin – Friends and Profile screens</title>
<link href="https://fonts.googleapis.com/css2?family=Nunito:wght@600;700;800&display=swap" rel="stylesheet">
<style>
  :root {
    --page-bg: #f1f1f1;
    --screen-bg: #fcefef;
    --screen-bg-alt: #f8ecef;
    --card-bg: #ffffff;
    --ink: #4a4a4a;
    --ink-soft: #5a5a5a;
    --yellow: #fdcb33;
    --pink: #f4436c;
    --teal-soft: #7dd9d0;
    --teal: #1fb5ac;
    --grey: #cfcfcf;
    --grey-line: #9a9a9a;
    --badge: #f4511e;
    --shadow: 0 3px 10px rgba(180, 140, 150, 0.18);
  }
  * { box-sizing: border-box; margin: 0; padding: 0; }
  html, body { width: 1200px; height: 981px; overflow: hidden; }
  body {
    background: var(--page-bg);
    font-family: "Nunito", sans-serif;
    color: var(--ink);
    position: relative;
  }
  .screen {
    position: absolute;
    top: 120px;
    width: 323px;
    height: 702px;
    border-radius: 34px;
    overflow: hidden;
    background: linear-gradient(180deg, var(--screen-bg) 0%, var(--screen-bg-alt) 100%);
    box-shadow: 0 10px 30px rgba(0, 0, 0, 0.08);
  }
  .screen--friends { left: 184px; }
  .screen--profile { left: 678px; }

  .screen-title {
    position: absolute;
    left: 18px;
    top: 42px;
    font-size: 20px;
    font-weight: 800;
    color: var(--ink-soft);
  }

  .card {
    position: absolute;
    left: 15px;
    width: 291px;
    height: 81px;
    background: var(--card-bg);
    border-radius: 6px;
    box-shadow: var(--shadow);
  }
  .avatar {
    position: absolute;
    left: 13px;
    top: 15px;
    width: 51px;
    height: 51px;
    border-radius: 50%;
  }
  .avatar--a { background: linear-gradient(135deg, #8a6d5a, #3e2d26); }
  .avatar--b { background: linear-gradient(135deg, #5b3a2c, #2a1a14); }
  .avatar--c { background: linear-gradient(135deg, #d9d1c4, #6e4c38); }
  .avatar--d { background: linear-gradient(135deg, #3f95c4, #b22630); }
  .avatar--e { background: linear-gradient(135deg, #f0ebe6, #6b4230); }
  .avatar--f { background: linear-gradient(135deg, #c9a24a, #5a6a2e); }
  .avatar--g { background: linear-gradient(135deg, #d8d8d8, #5c4a40); }

  .username {
    position: absolute;
    left: 74px;
    top: 31px;
    font-size: 11.5px;
    font-weight: 800;
    letter-spacing: 0.2px;
    color: var(--ink);
  }

  .action {
    position: absolute;
    top: 23px;
    width: 34px;
    height: 34px;
    border-radius: 50%;
    display: flex;
    align-items: center;
    justify-content: center;
  }
  .action--mail { left: 202px; }
  .action--like { left: 247px; }
  .action--idle { background: var(--grey); }
  .action--yellow { background: var(--yellow); }
  .action--pink { background: var(--pink); }
  .action svg { width: 20px; height: 20px; }

  .badge {
    position: absolute;
    top: -6px;
    right: -4px;
    width: 14px;
    height: 14px;
    border-radius: 50%;
    background: var(--badge);
    color: #fff;
    font-size: 9px;
    font-weight: 800;
    line-height: 14px;
    text-align: center;
  }

  .list-fade {
    position: absolute;
    left: 0;
    bottom: 0;
    width: 100%;
    height: 80px;
    background: linear-gradient(180deg, rgba(252, 239, 239, 0) 0%, rgba(248, 236, 239, 0.85) 70%);
  }

  .tab-bar {
    position: absolute;
    top: 614px;
    width: 218px;
    height: 52px;
    background: #fff;
    border-radius: 26px;
    box-shadow: 0 4px 14px rgba(0, 0, 0, 0.08);
  }
  .screen--friends .tab-bar { left: 52px; }
  .screen--profile .tab-bar { left: 53px; }
  .tab {
    position: absolute;
    top: 12px;
    width: 28px;
    height: 28px;
  }
  .tab svg { width: 28px; height: 28px; }
  .tab .badge { top: -4px; right: -4px; }

  .header-tools {
    position: absolute;
    right: 16px;
    top: 44px;
    display: flex;
    align-items: center;
    gap: 8px;
  }
  .header-tools svg { display: block; }

  .profile-head .avatar { left: 28px; top: 108px; }
  .profile-head .username { left: 89px; top: 124px; }

  .stat {
    position: absolute;
    top: 184px;
    width: 140px;
    height: 81px;
    border-radius: 6px;
    color: #fff;
    padding: 9px 12px;
  }
  .stat--quobarins { left: 16px; background: var(--yellow); }
  .stat--matched { left: 167px; background: var(--pink); }
  .stat-label { font-size: 11.5px; font-weight: 800; letter-spacing: 0.3px; }
  .stat-value { font-size: 20px; font-weight: 800; margin-top: 2px; letter-spacing: 0.5px; }

  .setting { left: 16px; }
  .setting-icon {
    position: absolute;
    left: 13px;
    top: 15px;
    width: 51px;
    height: 51px;
    border-radius: 50%;
    background: var(--teal-soft);
    display: flex;
    align-items: center;
    justify-content: center;
  }
  .setting-icon svg { width: 28px; height: 28px; }
  .setting-text {
    position: absolute;
    left: 74px;
    top: 24px;
    font-size: 11.5px;
    line-height: 14px;
    letter-spacing: 0.3px;
  }
  .setting-title { font-weight: 800; }
  .setting-value { font-weight: 600; }
  .chevron {
    position: absolute;
    right: 16px;
    top: 33px;
    width: 10px;
    height: 16px;
  }
</style>
</head>
<body>

<svg width="0" height="0" style="position:absolute" aria-hidden="true">
  <defs>
    <symbol id="icon-mail" viewBox="0 0 24 24">
      <rect x="3" y="5.5" width="18" height="13" rx="2" fill="none" stroke="#fff" stroke-width="1.6"/>
      <path d="M3.5 6.5 12 13l8.5-6.5" fill="none" stroke="#fff" stroke-width="1.6" stroke-linejoin="round"/>
    </symbol>
    <symbol id="icon-heart" viewBox="0 0 24 24">
      <path d="M12 20.5 4.4 13.2a4.7 4.7 0 0 1 6.7-6.6L12 7.5l.9-.9a4.7 4.7 0 0 1 6.7 6.6Z" fill="#fff"/>
    </symbol>
    <symbol id="icon-user" viewBox="0 0 28 28">
      <circle cx="14" cy="14" r="12" fill="none" stroke="currentColor" stroke-width="1.8"/>
      <circle cx="14" cy="11" r="3.6" fill="none" stroke="currentColor" stroke-width="1.8"/>
      <path d="M6.8 22.5c1.6-3.3 4.2-4.8 7.2-4.8s5.6 1.5 7.2 4.8" fill="none" stroke="currentColor" stroke-width="1.8"/>
    </symbol>
    <symbol id="icon-chat" viewBox="0 0 28 28">
      <path d="M4 5h20v14H11l-5 4.5V19H4Z" fill="none" stroke="currentColor" stroke-width="1.8" stroke-linejoin="round"/>
      <path d="M8.5 10h11M8.5 14h8" stroke="currentColor" stroke-width="1.8" stroke-linecap="round"/>
    </symbol>
    <symbol id="icon-radar" viewBox="0 0 28 28">
      <path d="M14 18.5 10.6 15a2.4 2.4 0 0 1 3.4-3.3 2.4 2.4 0 0 1 3.4 3.3Z" fill="none" stroke="currentColor" stroke-width="1.6" stroke-linejoin="round"/>
      <path d="M7.5 8.5a8 8 0 0 0 0 11M20.5 8.5a8 8 0 0 1 0 11M4 5.5a12.5 12.5 0 0 0 0 17M24 5.5a12.5 12.5 0 0 1 0 17" fill="none" stroke="currentColor" stroke-width="1.6" stroke-linecap="round"/>
    </symbol>
    <symbol id="icon-globe" viewBox="0 0 28 28">
      <circle cx="14" cy="14" r="12" fill="none" stroke="currentColor" stroke-width="1.8"/>
      <ellipse cx="14" cy="14" rx="5" ry="12" fill="none" stroke="currentColor" stroke-width="1.8"/>
      <path d="M2 14h24M4 8h20M4 20h20" stroke="currentColor" stroke-width="1.6"/>
    </symbol>
    <symbol id="icon-chevron" viewBox="0 0 10 16">
      <path d="M2 2l6 6-6 6" fill="none" stroke="#1fb5ac" stroke-width="2" stroke-linecap="round" stroke-linejoin="round"/>
    </symbol>
  </defs>
</svg>

<!-- Friends screen -->
<section class="screen screen--friends">
  <h1 class="screen-title">Friends</h1>

  <div class="card" style="top:91px">
    <div class="avatar avatar--a" role="img" aria-label="Friend profile photo"></div>
    <span class="username">Username</span>
    <span class="action action--mail action--idle"><svg><use href="#icon-mail"/></svg></span>
    <span class="action action--like action--yellow" role="img" aria-label="Send a quobarin"></span>
  </div>

  <div class="card" style="top:184px">
    <div class="avatar avatar--b" role="img" aria-label="Friend profile photo"></div>
    <span class="username">Username</span>
    <span class="action action--mail action--yellow"><svg><use href="#icon-mail"/></svg><span class="badge">1</span></span>
    <span class="action action--like action--pink"><svg><use href="#icon-heart"/></svg><span class="badge">1</span></span>
  </div>

  <div class="card" style="top:277px">
    <div class="avatar avatar--c" role="img" aria-label="Friend profile photo"></div>
    <span class="username">Username</span>
    <span class="action action--mail action--idle"><svg><use href="#icon-mail"/></svg></span>
    <span class="action action--like action--yellow" role="img" aria-label="Send a quobarin"></span>
  </div>

  <div class="card" style="top:370px">
    <div class="avatar avatar--d" role="img" aria-label="Friend profile photo"></div>
    <span class="username">Username</span>
    <span class="action action--mail action--idle"><svg><use href="#icon-mail"/></svg></span>
    <span class="action action--like action--yellow" role="img" aria-label="Send a quobarin"></span>
  </div>

  <div class="card" style="top:463px">
    <div class="avatar avatar--e" role="img" aria-label="Friend profile photo"></div>
    <span class="username">Username</span>
    <span class="action action--mail action--yellow"><svg><use href="#icon-mail"/></svg></span>
    <span class="action action--like action--pink"><svg><use href="#icon-heart"/></svg><span class="badge">1</span></span>
  </div>

  <div class="card" style="top:556px">
    <div class="avatar avatar--f" role="img" aria-label="Friend profile photo"></div>
    <span class="username">Username</span>
    <span class="action action--mail action--idle"><svg><use href="#icon-mail"/></svg></span>
    <span class="action action--like action--yellow" role="img" aria-label="Send a quobarin"></span>
  </div>

  <div class="card" style="top:649px">
    <div class="avatar avatar--g" role="img" aria-label="Friend profile photo"></div>
    <span class="username">Username</span>
    <span class="action action--mail action--idle"><svg><use href="#icon-mail"/></svg></span>
    <span class="action action--like action--yellow" role="img" aria-label="Send a quobarin"></span>
  </div>

  <div class="list-fade"></div>

  <nav class="tab-bar">
    <span class="tab" style="left:19px;color:var(--grey-line)"><svg><use href="#icon-user"/></svg></span>
    <span class="tab" style="left:69px;color:var(--teal)"><svg><use href="#icon-chat"/></svg><span class="badge">3</span></span>
    <span class="tab" style="left:121px;color:var(--grey-line)"><svg><use href="#icon-radar"/></svg></span>
    <span class="tab" style="left:172px;color:var(--grey-line)"><svg><use href="#icon-globe"/></svg></span>
  </nav>
</section>

<!-- Profile screen -->
<section class="screen screen--profile">
  <h1 class="screen-title">Profile</h1>
  <div class="header-tools">
    <svg width="24" height="8" viewBox="0 0 24 8" aria-label="More">
      <circle cx="4" cy="4" r="2.8" fill="none" stroke="#5a5a5a" stroke-width="1.4"/>
      <circle cx="12" cy="4" r="2.8" fill="none" stroke="#5a5a5a" stroke-width="1.4"/>
      <circle cx="20" cy="4" r="2.8" fill="none" stroke="#5a5a5a" stroke-width="1.4"/>
    </svg>
    <svg width="22" height="22" viewBox="0 0 24 24" aria-label="Settings">
      <path d="M12 1.8l2 .3.5 2.6 1.6.9 2.4-1.1 1.5 1.4-1.1 2.4.9 1.6 2.6.5.3 2-.3 2-2.6.5-.9 1.6 1.1 2.4-1.5 1.4-2.4-1.1-1.6.9-.5 2.6-2 .3-2-.3-.5-2.6-1.6-.9-2.4 1.1L4 19.4l1.1-2.4-.9-1.6-2.6-.5L1.3 13v-2l.3-.1 2.6-.5.9-1.6L4 6.4l1.5-1.4 2.4 1.1 1.6-.9.5-2.6Z" fill="none" stroke="#5a5a5a" stroke-width="1.4" stroke-linejoin="round"/>
      <circle cx="12" cy="12" r="3.6" fill="none" stroke="#5a5a5a" stroke-width="1.4"/>
    </svg>
  </div>

  <div class="profile-head">
    <div class="avatar avatar--a" role="img" aria-label="User profile photo"></div>
    <span class="username">Username</span>
  </div>

  <div class="stat stat--quobarins">
    <div class="stat-label">Quobarins</div>
    <div class="stat-value">56</div>
  </div>
  <div class="stat stat--matched">
    <div class="stat-label">Matched</div>
    <div class="stat-value">76%</div>
  </div>

  <div class="card setting" style="top:277px">
    <span class="setting-icon">
      <svg viewBox="0 0 28 28"><path d="M14 25s-7.5-8-7.5-13.2a7.5 7.5 0 0 1 15 0C21.5 17 14 25 14 25Z" fill="none" stroke="#fff" stroke-width="1.8" stroke-linejoin="round"/><circle cx="14" cy="11.5" r="3" fill="none" stroke="#fff" stroke-width="1.8"/></svg>
    </span>
    <div class="setting-text">
      <div class="setting-title">Contact</div>
      <div class="setting-value">Marrowlane 218, Fenbury</div>
    </div>
    <svg class="chevron"><use href="#icon-chevron"/></svg>
  </div>

  <div class="card setting" style="top:370px">
    <span class="setting-icon">
      <svg viewBox="0 0 28 28"><path d="M7.5 20V13a6.5 6.5 0 0 1 13 0v7l1.5 1.5H6Z" fill="none" stroke="#fff" stroke-width="1.8" stroke-linejoin="round"/><path d="M12 23.5h4" stroke="#fff" stroke-width="1.8" stroke-linecap="round"/></svg>
    </span>
    <div class="setting-text">
      <div class="setting-title">Push notifications</div>
      <div class="setting-value">Show in Lockscreen</div>
    </div>
    <svg class="chevron"><use href="#icon-chevron"/></svg>
  </div>

  <div class="card setting" style="top:463px">
    <span class="setting-icon">
      <svg viewBox="0 0 28 28"><circle cx="14" cy="14" r="11" fill="none" stroke="#fff" stroke-width="1.8"/><path d="M14 12.5v7" stroke="#fff" stroke-width="1.8" stroke-linecap="round"/><circle cx="14" cy="9" r="1.2" fill="#fff"/></svg>
    </span>
    <div class="setting-text">
      <div class="setting-title">Language</div>
      <div class="setting-value">English</div>
    </div>
    <svg class="chevron"><use href="#icon-chevron"/></svg>
  </div>

  <div class="card setting" style="top:557px">
    <span class="setting-icon">
      <svg viewBox="0 0 28 28"><path d="M10 8V5h12v18H10v-3" fill="none" stroke="#fff" stroke-width="1.8" stroke-linejoin="round"/><path d="M5 14h11M13 10.5l3.5 3.5-3.5 3.5" fill="none" stroke="#fff" stroke-width="1.8" stroke-linecap="round" stroke-linejoin="round"/></svg>
    </span>
    <div class="setting-text">
      <div class="setting-title">Logout</div>
      <div class="setting-value">App Logout</div>
    </div>
    <svg class="chevron"><use href="#icon-chevron"/></svg>
  </div>

  <nav class="tab-bar">
    <span class="tab" style="left:17px;color:var(--teal)"><svg><use href="#icon-user"/></svg></span>
    <span class="tab" style="left:67px;color:var(--grey-line)"><svg><use href="#icon-chat"/></svg><span class="badge">3</span></span>
    <span class="tab" style="left:121px;color:var(--grey-line)"><svg><use href="#icon-radar"/></svg></span>
    <span class="tab" style="left:172px;color:var(--grey-line)"><svg><use href="#icon-globe"/></svg></span>
  </nav>
</section>

</body>
</html>
```